Website Design & Development For a New Start Up

We require a bespoke website design and development.
Requirements:
We want something similar to www.pelmorabank.com... not exact as this is copywrite infringement... but we want you to get a feel for the site and design accordingly. We will leave the creativity to you.
All logos, detailed content and description will be given upon seeing the designs and your eye for creativity. here are our requirements.
1. Upto 20 internal pages. Clean simple design that will be discussed with developer.
2. Account Opening sections - Very detailed client sign up. 4 types of client to sign up (Bespoke account information required for each client)
3. Client Login Area. Client Authentication tools.
4. Admin and Client area - where documents and information will be stored.
5. Live API currency feeds into front end.
6. Document security and Website security is very important as we will be holding client information
7. We want the website to be RESPONSIVE on ALL smart Phones and Tablyx etc. Website MUST work on all browsers regardless of age.
8. We would like ALL coding to be done in CLEAN HTML5 and it must work effortlessly for clients when they touch any button etc.
We want a designer and developer that has the eye for intricate aesthetic design and technical ability to execute functional perfectly and make the user experience effortless.
We look forward to seeing your designs and working with you.
Regards
Quarlen Team
Reason: We are still getting designs and we have yet to get it perfected so we are waiting for more submissions. Thanks
Financial Money Transaction
Security

```html
<!DOCTYPE html>
<html lang="en">
<head>
<meta charset="utf-8">
<title>Money Without Borders</title>
<link href="https://fonts.googleapis.com/css2?family=Pathway+Gothic+One&family=Arimo:wght@400;700&display=swap" rel="stylesheet">
<style>
:root{
  --blue:#1a86c7;
  --blue-dark:#1573ab;
  --orange:#f57b1f;
  --ink:#333;
  --muted:#8a8a8a;
  --header:#2b2e31;
  --band:#2d2d2d;
  --footer:#333537;
  --bar:#262728;
  --white:#fff;
}
*{box-sizing:border-box;margin:0;padding:0}
html,body{width:738px;height:1200px;overflow:hidden;background:var(--white)}
body{position:relative;font-family:"Arimo",Arial,sans-serif;color:var(--ink)}
.abs{position:absolute}
.cond{font-family:"Pathway Gothic One","Arial Narrow",sans-serif;text-transform:uppercase}

/* header */
.site-header{left:0;top:0;width:738px;height:66px;background:var(--header)}
.brand-name{left:105px;top:25px;font-family:"Arimo",Arial,sans-serif;font-weight:700;font-size:15px;color:var(--white);letter-spacing:.4px}
.main-nav{left:302px;top:40px;display:flex;font-size:7.5px;color:#d8d8d8}
.main-nav span{margin-right:20px}
.main-nav .active{color:var(--blue)}

/* hero */
.hero{left:0;top:66px;width:738px;height:346px;background:linear-gradient(180deg,#2b4766 0%,#3f6f95 30%,#2d4f6c 60%,#1c2b3a 100%)}
.transfer-panel{left:230px;top:118px;width:277px;height:172px;background:rgba(255,255,255,.55);border-radius:5px}
.panel-title{left:253px;top:139px;width:232px;height:24px;background:var(--blue);color:var(--white);font-size:13px;text-align:center;line-height:24px}
.field-label{font-size:12.5px;color:#2a2a2a}
.field{height:17px;background:var(--white);border-radius:2px;color:var(--orange);font-family:"Pathway Gothic One",sans-serif;font-size:10px;line-height:17px;padding-left:6px}
.field.select{width:52px}
.field.select::after{content:"\2195";position:absolute;right:5px;color:#555;font-size:8px}
.field.currency{width:52px}
.rate-bar{left:253px;top:243px;width:232px;height:24px;background:var(--orange);color:var(--white);font-size:9.5px;line-height:24px;padding-left:11px}
.send-btn{left:421px;top:248px;width:47px;height:14px;background:var(--white);color:var(--orange);font-size:9px;text-align:center;line-height:14px}
.hero-tabs{left:98px;top:361px;width:542px;height:51px;display:flex}
.hero-tabs div{flex:1;background:var(--blue);color:var(--white);font-size:16px;text-align:center;line-height:51px}
.hero-tabs div:nth-child(2),.hero-tabs div:nth-child(4){background:var(--blue-dark)}

/* about band */
.about-band{left:0;top:412px;width:738px;height:72px;background:var(--band)}
.about-title{left:121px;top:430px;font-size:30px;color:var(--white)}
.about-title span{color:var(--blue)}
.about-rule{left:232px;top:436px;width:1px;height:24px;background:#666}
.about-text{left:255px;top:429px;width:380px;font-size:7.2px;line-height:12.5px;color:#6f6f6f}
.about-more{left:597px;top:465px;font-size:8px;color:#ddd}

/* cards */
.card{top:529px;width:158px;height:143px;background:var(--white);box-shadow:0 0 4px rgba(0,0,0,.2);text-align:center}
.card h3{font-weight:400;font-size:14px;color:#333;margin-top:19px}
.card p{font-size:7.2px;line-height:12.2px;color:#8a8a8a;text-align:justify;text-align-last:center;padding:0 21px;margin-top:12px}
.card .learn{font-size:8px;color:var(--blue);margin-top:12px}

/* welcome */
.welcome-title{left:98px;top:720px;font-size:17px;color:#333}
.welcome-title span{color:var(--blue)}
.feature-icon{left:98px;width:48px;height:41px}
.feature h4{font-weight:400;font-size:13px;color:#333}
.feature p{font-size:7.2px;line-height:12.5px;color:#777;margin-top:3px}
.video{left:341px;top:726px;width:288px;height:200px;background:linear-gradient(135deg,#d7dde3 0%,#b9c3cc 45%,#6e7a86 100%)}
.play{left:453px;top:792px}

/* footer */
.site-footer{left:0;top:976px;width:738px;height:198px;background:linear-gradient(180deg,#3a3c3e,#2e3032)}
.footer-heading{font-size:16px;color:var(--white);text-align:center;width:160px}
.footer-text{font-size:7.6px;line-height:13.2px;color:#cfcfcf;width:118px;text-align:justify}
.quote{font-family:Georgia,serif;font-size:20px;color:#aaa}
.arrow-btn{width:15px;height:15px}
.author{font-size:8px;font-weight:700;font-style:italic;color:#eee}
.input{left:486px;width:138px;height:14px;background:#f1f1f1;border-radius:2px;font-size:6.5px;color:#999;padding:3px 6px}
.send{left:592px;top:1131px;width:32px;height:12px;background:#8b8d8f;border-radius:2px;color:var(--white);font-size:7px;text-align:center;line-height:12px}
.bottom-bar{left:0;top:1174px;width:738px;height:26px;background:var(--bar)}
.copyright{left:183px;top:1183px;font-size:6.5px;color:#888}
.social{top:1181px;width:11px;height:11px;background:#4a4b4d;border-radius:1px}
</style>
</head>
<body>

<header class="abs site-header">
  <div class="abs brand-name">MERIDANE</div>
  <nav class="abs main-nav">
    <span class="active">HOME</span><span>ABOUT US</span><span>SERVICES</span><span>ARCHIVES</span><span>LOCATIONS</span><span>AGENTS</span><span>CONTACT US</span>
  </nav>
</header>

<section class="abs hero" role="img" aria-label="Aerial evening view of a coastal city with beach and high-rise lights"></section>

<div class="abs transfer-panel"></div>
<div class="abs panel-title cond">Send Money Overseas</div>
<div class="abs field-label cond" style="left:283px;top:186px">You Pay</div>
<div class="abs field select" style="left:325px;top:186px">1,000.00</div>
<div class="abs field-label cond" style="left:387px;top:186px">From</div>
<div class="abs field currency" style="left:416px;top:186px">GBP</div>
<div class="abs field-label cond" style="left:258px;top:210px">Reciever Gets</div>
<div class="abs field select" style="left:325px;top:210px">1,523.12</div>
<div class="abs field-label cond" style="left:399px;top:210px">To</div>
<div class="abs field currency" style="left:416px;top:210px">USD</div>
<div class="abs rate-bar cond">Service Charges = 0.00 , Exchange Rate = 2.034</div>
<div class="abs send-btn cond">Send Now</div>

<div class="abs hero-tabs cond">
  <div>Sighn Up</div><div>Login</div><div>Help</div><div>How It Works</div>
</div>

<section class="abs about-band"></section>
<h2 class="abs about-title cond" style="font-weight:400">About <span>Us</span></h2>
<div class="abs about-rule"></div>
<p class="abs about-text">Lorem Ipsum is simply dummy text of the printing and typesetting industry. Lorem Ipsum has been the industry's standard dummy text ever since the 1500s, when an unknown printer took a galley of type and scrambled it to make a type specimen book. It has survived not only five centuries,</p>
<div class="abs about-more cond">Learn More</div>

<article class="abs card" style="left:98px"><h3 class="cond">Send &amp; Receive Money</h3><p>orem Ipsum is simply dummy text of the printing and typesetting industry. Lorem Ipsum has been the industry's standard dummy text</p><div class="learn">LEARN MORE</div></article>
<article class="abs card" style="left:290px"><h3 class="cond">Benefits</h3><p>orem Ipsum is simply dummy text of the printing and typesetting industry. Lorem Ipsum has been the industry's standard dummy text</p><div class="learn">LEARN MORE</div></article>
<article class="abs card" style="left:482px"><h3 class="cond">Offers</h3><p>orem Ipsum is simply dummy text of the printing and typesetting industry. Lorem Ipsum has been the industry's standard dummy text</p><div class="learn">LEARN MORE</div></article>

<h2 class="abs welcome-title cond" style="font-weight:400">Welcome to <span>Money Without Borders</span></h2>

<svg class="abs feature-icon" style="top:760px" viewBox="0 0 48 41"><rect width="48" height="41" fill="#1a86c7"/><circle cx="24" cy="20.5" r="13" fill="none" stroke="#fff" stroke-width="3"/><text x="24" y="26" text-anchor="middle" font-family="Arial" font-weight="700" font-size="15" fill="#fff">$</text></svg>
<div class="abs feature" style="left:160px;top:758px"><h4 class="cond">10 Times Lower Cost.</h4><p>Banks charge 5% in hidden fees.<br>People on Pelmora pay 0.5%.</p></div>

<svg class="abs feature-icon" style="top:823px" viewBox="0 0 48 41"><rect x="1" y="1" width="46" height="39" fill="#fff" stroke="#1a86c7" stroke-width="1.5"/><path d="M10 30a14 14 0 0 1 28 0" fill="none" stroke="#1a86c7" stroke-width="4"/><line x1="24" y1="30" x2="33" y2="22" stroke="#1a86c7" stroke-width="3"/><circle cx="24" cy="30" r="3" fill="#1a86c7"/></svg>
<div class="abs feature" style="left:160px;top:821px"><h4 class="cond">Faster, Simpler.</h4><p>Tap in how much and where to.<br>Upload money, let the magic happen.</p></div>

<svg class="abs feature-icon" style="top:886px" viewBox="0 0 48 41"><rect x="1" y="1" width="46" height="39" fill="#fff" stroke="#1a86c7" stroke-width="1.5"/><path d="M11 15 24 8l13 7z" fill="#1a86c7"/><rect x="13" y="17" width="3" height="13" fill="#1a86c7"/><rect x="19" y="17" width="3" height="13" fill="#1a86c7"/><rect x="26" y="17" width="3" height="13" fill="#1a86c7"/><rect x="32" y="17" width="3" height="13" fill="#1a86c7"/><rect x="11" y="31" width="26" height="3" fill="#1a86c7"/></svg>
<div class="abs feature" style="left:160px;top:884px"><h4 class="cond">Outsmart Your Bank.</h4><p>A totally new way to beat the old system,<br>founded on fairness</p></div>

<div class="abs video" role="img" aria-label="Video still of a business team gathered around a laptop in a bright office"></div>
<svg class="abs play" width="64" height="64" viewBox="0 0 64 64"><circle cx="32" cy="32" r="29" fill="none" stroke="rgba(255,255,255,.85)" stroke-width="4"/><path d="M25 18 47 32 25 46z" fill="rgba(255,255,255,.85)"/></svg>

<footer class="abs site-footer" role="img" aria-label="Dim city skyline backdrop"></footer>
<h3 class="abs footer-heading cond" style="left:97px;top:1010px;font-weight:400">Client Testimonials</h3>
<h3 class="abs footer-heading cond" style="left:291px;top:1010px;font-weight:400">Our Services</h3>
<h3 class="abs footer-heading cond" style="left:480px;top:1010px;font-weight:400">Contact Us</h3>

<div class="abs quote" style="left:100px;top:1036px">&ldquo;</div>
<p class="abs footer-text" style="left:119px;top:1044px">Lorem Ipsum is simply dummy text of the printing and typeset-ting industry. Lorem Ipsum has been the industry's standard dummy text ever since the</p>
<div class="abs quote" style="left:240px;top:1098px">&rdquo;</div>
<svg class="abs arrow-btn" style="left:121px;top:1121px" viewBox="0 0 15 15"><rect width="15" height="15" fill="#5a5c5e"/><path d="M9 4 5.5 7.5 9 11" fill="none" stroke="#fff" stroke-width="1.5"/></svg>
<svg class="abs arrow-btn" style="left:141px;top:1121px" viewBox="0 0 15 15"><rect width="15" height="15" fill="#5a5c5e"/><path d="M6 4l3.5 3.5L6 11" fill="none" stroke="#fff" stroke-width="1.5"/></svg>
<div class="abs author" style="left:193px;top:1129px">JAMES SMITH</div>

<p class="abs footer-text" style="left:313px;top:1044px">Lorem Ipsum is simply dummy text of the printing and typeset-ting industry. Lorem Ipsum has been the industry's standard dummy text ever since the</p>
<div class="abs" style="left:370px;top:1129px;font-size:8px;color:#ddd">LEARN MORE</div>

<div class="abs input" style="top:1047px">NAME</div>
<div class="abs input" style="top:1068px">EMAIL</div>
<div class="abs input" style="top:1088px;height:36px">MESSAGE</div>
<div class="abs send">SEND</div>

<div class="abs bottom-bar"></div>
<div class="abs copyright">&copy; 2015&nbsp; MERIDANE . All Rights Reserved &nbsp;|&nbsp; Powered by Brightlane</div>
<div class="abs social" style="left:518px"></div>
<div class="abs social" style="left:533px"></div>
<div class="abs social" style="left:548px"></div>
<div class="abs social" style="left:563px"></div>
<div class="abs social" style="left:578px"></div>

</body>
</html>
```